Briarwood Homes Lakeshore Customer Brochure

Need a brochure designed that is clean and minimal that contains our logo, and contact information. Would like an area where we could insert business cards, and slips on both sides of the openings to place sheets of paper in. Would prefer to have the COVER LETTER I have attached printed on one side of the opening.

Target Market(s)

Home buyers

Font styles to use
Sans Serif

Colors

Designer to choose colors to be used in the design.

Requirements
Must have
• Logo, contact info, website, etc. Must be minimal in design and very clean looking.
Nice to have
• Please see above
Should not have
• No stock pictures of homes, builds, etc. Need it to look very clean

```html
<!DOCTYPE html>
<html lang="en">
<head>
<meta charset="utf-8">
<title>Briarwood Homes Lakeshore – Presentation Folder</title>
<link rel="stylesheet" href="https://fonts.googleapis.com/css2?family=Oswald:wght@300;400&family=Archivo:wght@700&display=swap">
<style>
  :root {
    --backdrop: #d2d3d5;
    --folder: #353334;
    --folder-deep: #2c2a2b;
    --pocket: #363435;
    --gutter: #262425;
    --tan: #d2a679;
    --white: #ffffff;
    --slit: #8a8889;
  }
  * { margin: 0; padding: 0; box-sizing: border-box; }
  html, body { width: 1200px; height: 1070px; overflow: hidden; background: var(--backdrop); }
  .folder { position: relative; width: 1200px; height: 1070px; }

  .panel {
    position: absolute;
    top: 92px;
    height: 626px;
    background: var(--folder);
  }
  .panel--inside-left { left: 116px; width: 485px; }
  .panel--inside-right {
    left: 601px; width: 482px;
    background: linear-gradient(90deg, var(--gutter) 0, var(--folder) 14px, var(--folder) 94%, var(--folder-deep) 100%);
  }

  .home-photo {
    position: absolute;
    left: 0; top: 60px; width: 100%; height: 480px;
    background: linear-gradient(180deg, #363435 0%, #3b393a 45%, #333132 100%);
  }

  .wordmark {
    position: absolute;
    left: 0; right: 0;
    display: flex; align-items: center; justify-content: center; gap: 10px;
    font-family: "Archivo", Arial, sans-serif;
    font-weight: 700;
    color: var(--white);
    letter-spacing: 0.02em;
    line-height: 1;
  }
  .wordmark__square { background: var(--tan); display: block; }
  .panel--inside-left .wordmark { top: 464px; font-size: 21px; }
  .panel--inside-left .wordmark__square { width: 16px; height: 16px; }
  .panel--inside-right .wordmark { top: 395px; font-size: 33px; gap: 14px; }
  .panel--inside-right .wordmark__square { width: 24px; height: 24px; }

  .contact {
    position: absolute;
    left: 0; right: 0; top: 535px;
    text-align: center;
    font-family: "Oswald", Arial, sans-serif;
    font-style: normal;
    font-weight: 300;
    color: var(--white);
    font-size: 11px;
    line-height: 19px;
    letter-spacing: -0.02em;
  }

  .website {
    position: absolute;
    left: 0; right: 0; top: 551px;
    text-align: center;
    font-family: "Oswald", Arial, sans-serif;
    font-weight: 300;
    font-size: 19px;
    letter-spacing: 0.12em;
    color: var(--white);
  }

  .pockets { position: absolute; left: 0; top: 0; }
</style>
</head>
<body>
<main class="folder">
  <section class="panel panel--inside-left">
    <div class="home-photo" role="img" aria-label="Faded dark photo of a two-storey home facade"></div>
    <div class="wordmark"><span class="wordmark__square"></span>BRIARWOOD HOMES</div>
    <address class="contact">
      88 HARBOURVIEW RD. PORT DALHOUSIE, ONTARIO, L2N 4K7. TEL: 905-555-0142 FAX: 905-555-0177<br>
      WWW.BRIARWOODHOMESLAKESHORE.COM
    </address>
  </section>

  <section class="panel panel--inside-right">
    <div class="wordmark"><span class="wordmark__square"></span>BRIARWOOD HOMES</div>
    <p class="website">WWW.BRIARWOODHOMESLAKESHORE.COM</p>
  </section>

  <svg class="pockets" width="1200" height="1070" viewBox="0 0 1200 1070" aria-hidden="true">
    <polygon class="pocket pocket--left" points="116,718 600,718 576,944 116,944" fill="#363435"/>
    <polygon class="pocket pocket--right" points="602,718 1086,718 1086,944 628,944" fill="#363435"/>
    <line class="card-slit" x1="242" y1="793" x2="272" y2="766" stroke="#8a8889" stroke-width="1"/>
    <line class="card-slit" x1="436" y1="898" x2="466" y2="870" stroke="#8a8889" stroke-width="1"/>
  </svg>
</main>
</body>
</html>
```